Ember Drift Product Package Design

Hi all,
We are starting our personal/portable vaporizer company and in the process of finishing our product, designed in California by our own engineer. It will have a LCD screen plus 3 different tanks for e-liquid, essential oil, and loose-leaf. We have a logo already and sample box of what we wanted, but we are in need of someone who can help design our product package - color, placement logo, etc.; our sample box is inspired by Pulse by Nico.
We want the logo "ED" to be somewhat raised - like how verlane symbol is on the watch - on the sleeve of the box and the "ember drift" on the main box embossed or laser etched.. not sure. Our slogan, Chase your drift, needs to be inside of the box when you open. but then again, whatever looks best. we want it chic, simple yet classy. Material for the main box/sleeve: matte finish or dana forell dark brown box package feel.
I'll upload our logo and text. You guys can play around with it to get the perfect design we'll want.
The chaseurdriftpen.png is a sample pic of our product, so you have an idea of how it looks like.
Competitors: Kiro by trell, LOMUX, G, etc.
See Sam Brell Packaging

```html
<!DOCTYPE html>
<html lang="en">
<head>
<meta charset="utf-8">
<title>Ember Drift — Sleeve Design</title>
<link rel="stylesheet" href="https://fonts.googleapis.com/css2?family=Cinzel:wght@500&family=Poiret+One&family=Open+Sans:wght@400&display=swap">
<style>
  :root {
    --backdrop: #c8b19a;
    --sleeve: #030304;
    --ink-soft: #9c8d86;
    --ember: #d5955a;
    --url: #b9b9bd;
    --smoke-core: #e8ecf6;
    --smoke-mid: #5d6478;
    --wave-tone: #8a8b92;
  }
  html, body {
    margin: 0;
    padding: 0;
    width: 1200px;
    height: 798px;
    overflow: hidden;
    background: var(--backdrop);
  }
  .sleeve-sheet {
    position: absolute;
    left: 160px;
    top: 33px;
    width: 880px;
    height: 732px;
    filter: drop-shadow(-6px 6px 6px rgba(0,0,0,0.35));
  }
  .brand-name {
    font-family: "Cinzel", serif;
    font-weight: 500;
    font-size: 20px;
    letter-spacing: 8px;
    fill: var(--ember);
  }
  .slogan-lead {
    font-family: "Poiret One", sans-serif;
    font-size: 24px;
    letter-spacing: 2px;
    fill: var(--ink-soft);
  }
  .slogan-key {
    font-family: "Poiret One", sans-serif;
    font-size: 40px;
    letter-spacing: 6px;
    fill: var(--ember);
  }
  .site-url {
    font-family: "Open Sans", sans-serif;
    font-size: 12px;
    fill: var(--url);
  }
</style>
</head>
<body>
<svg class="sleeve-sheet" viewBox="0 0 880 732" xmlns="http://www.w3.org/2000/svg">
  <defs>
    <radialGradient id="smoke-glow" cx="50%" cy="50%" r="50%">
      <stop offset="0%" stop-color="var(--smoke-core)" stop-opacity="0.95"/>
      <stop offset="30%" stop-color="var(--smoke-mid)" stop-opacity="0.7"/>
      <stop offset="100%" stop-color="var(--sleeve)" stop-opacity="0"/>
    </radialGradient>
    <linearGradient id="wave-sheen" x1="0" y1="0" x2="0" y2="1">
      <stop offset="0%" stop-color="var(--wave-tone)" stop-opacity="0"/>
      <stop offset="50%" stop-color="var(--wave-tone)" stop-opacity="0.35"/>
      <stop offset="100%" stop-color="var(--wave-tone)" stop-opacity="0"/>
    </linearGradient>
    <linearGradient id="slogan-plate" x1="0" y1="0" x2="0" y2="1">
      <stop offset="0%" stop-color="#2a1512"/>
      <stop offset="100%" stop-color="#0d0706"/>
    </linearGradient>
  </defs>

  <path class="sleeve-body" fill="var(--sleeve)"
        d="M0 0 H880 V342 A22 22 0 0 0 880 386 V732 H0 V386 A22 22 0 0 0 0 342 Z"/>

  <rect class="smoke-left" role="img" aria-label="Drifting smoke lit from within"
        x="0" y="164" width="186" height="256" fill="url(#smoke-glow)"/>
  <rect class="smoke-right" role="img" aria-label="Drifting smoke lit from within"
        x="609" y="115" width="271" height="389" fill="url(#smoke-glow)"/>
  <rect class="smoke-logo" role="img" aria-label="Soft smoke glow behind the brand mark"
        x="273" y="92" width="332" height="259" fill="url(#smoke-glow)"/>

  <g class="brand-lockup">
    <rect class="brand-square" x="405" y="200" width="70" height="70" fill="var(--ember)"/>
    <text class="brand-name" x="444" y="336" text-anchor="middle">EMBER DRIFT</text>
  </g>

  <path class="wave-band" role="img" aria-label="Flowing band of fine silver wave lines"
        d="M0 560 C220 520 420 560 560 580 S780 560 880 460 V640 C780 660 640 660 520 640 S200 600 0 670 Z"
        fill="url(#wave-sheen)"/>

  <rect class="slogan-plate" x="348" y="476" width="203" height="94" fill="url(#slogan-plate)"/>
  <text class="slogan-lead" x="450" y="507" text-anchor="middle">CHASE YOUR</text>
  <text class="slogan-key" x="450" y="552" text-anchor="middle">DRIFT</text>
  <text class="site-url" x="450" y="581" text-anchor="middle">www.EmberDrift.com</text>
</svg>
</body>
</html>
```